VelloPath Business Card

Our company is called VelloPath and we are based in Tel Aviv, Israel. We create innovative and exciting methods for getting people on the web engaged with content. We need a cool yet professional business card that will represent our management level employees. keep in mind this is a start up company with a young atmosphere. You can be inspired by our logo (file attached, make sure you have the right font "Ubuntu-Condensed") Use the colors that are used in the logo and create a colourful and professional business card.

```html
<!DOCTYPE html>
<html lang="en">
<head>
<meta charset="utf-8">
<title>VelloPath Business Card</title>
<link rel="stylesheet" href="https://fonts.googleapis.com/css2?family=Ubuntu+Condensed&display=swap">
<style>
  :root {
    --backdrop: #dcdcdd;
    --card-white: #ffffff;
    --card-dark: #252525;
    --ink-dark: #222222;
    --ink-light: #ffffff;
    --label-blue: #4a8fcf;
    --accent-orange: #e6a93a;
    --accent-magenta: #c2207c;
    --accent-blue: #86bde3;
    --brand-dot: #c2207c;
  }
  * { margin: 0; padding: 0; box-sizing: border-box; }
  html, body {
    width: 1200px;
    height: 1200px;
    overflow: hidden;
    background: var(--backdrop);
    font-family: "Ubuntu Condensed", "Arial Narrow", sans-serif;
  }
  .canvas {
    position: relative;
    width: 1200px;
    height: 1200px;
  }
  .card {
    position: absolute;
    top: 261px;
    width: 399px;
    height: 716px;
    overflow: hidden;
  }
  .card--front { left: 141px; background: var(--card-white); }
  .card--back { left: 659px; background: var(--card-dark); }

  .front-base {
    position: absolute;
    left: 0;
    top: 0;
    width: 399px;
    height: 716px;
  }
  .line {
    position: absolute;
    left: 0;
    right: 0;
    text-align: center;
    transform: translateY(-50%);
    white-space: nowrap;
  }
  .wordmark {
    display: flex;
    align-items: center;
    justify-content: center;
    gap: 12px;
  }
  .wordmark__dot {
    width: 28px;
    height: 28px;
    border-radius: 50%;
  }
  .wordmark__name { font-size: 46px; line-height: 1; }

  .card--front .wordmark { top: 190px; }
  .card--front .wordmark__dot { background: var(--brand-dot); }
  .card--front .wordmark__name { color: var(--ink-dark); }

  .holder-name { top: 386px; font-size: 44px; color: var(--ink-light); }
  .holder-role { top: 432px; font-size: 30px; color: var(--ink-light); }

  .contact { font-size: 25px; color: var(--ink-light); }
  .contact__label { color: var(--label-blue); }
  .contact--phone { top: 518px; }
  .contact--web { top: 567px; }
  .contact--email { top: 614px; }

  .tagline {
    position: absolute;
    left: 0;
    right: 0;
    top: 104px;
    text-align: center;
    color: var(--ink-light);
    font-size: 46px;
    line-height: 65px;
  }
  .card--back .wordmark { top: 608px; gap: 10px; }
  .card--back .wordmark__dot { width: 20px; height: 20px; background: var(--ink-light); }
  .card--back .wordmark__name { font-size: 32px; color: var(--ink-light); }
</style>
</head>
<body>
<main class="canvas">
  <section class="card card--front">
    <svg class="front-base" viewBox="0 0 300 540" preserveAspectRatio="none" role="img" aria-label="Colourful curved accent band above the dark contact area">
      <defs>
        <linearGradient id="accent-wash" x1="0" y1="0" x2="1" y2="0">
          <stop offset="0" stop-color="var(--accent-orange)"/>
          <stop offset="0.5" stop-color="var(--accent-magenta)"/>
          <stop offset="1" stop-color="var(--accent-blue)"/>
        </linearGradient>
      </defs>
      <path d="M0,262 Q150,162 300,262 V540 H0 Z" fill="url(#accent-wash)"/>
      <path d="M0,300 Q150,184 300,300 V540 H0 Z" fill="var(--card-dark)"/>
    </svg>
    <div class="line wordmark">
      <span class="wordmark__dot"></span>
      <span class="wordmark__name">VelloPath</span>
    </div>
    <p class="line holder-name">Name</p>
    <p class="line holder-role">(position)</p>
    <p class="line contact contact--phone"><span class="contact__label">Phone</span>: +000 123 456 789</p>
    <p class="line contact contact--web"><span class="contact__label">Web</span>: www.vellopath.com</p>
    <p class="line contact contact--email"><span class="contact__label">Email</span>: name@vellopath.com</p>
  </section>

  <section class="card card--back">
    <p class="tagline">Shape<br>your<br>dreams<br>with<br>us</p>
    <div class="line wordmark">
      <span class="wordmark__dot"></span>
      <span class="wordmark__name">VelloPath</span>
    </div>
  </section>
</main>
</body>
</html>
```